Shopify Design for Back Pain Patch

We need a design for the Shopify-based homepage of the new Vorlixa Spine Pad.

The Vorlixa spine pad absorbs the surface energy produced by your body when you are in pain and redistributes it, reducing your discomfort. It is approximately 5” x 5” in size, with an adhesive backing on one side and a cloth-like exterior that is neutral/light tan in color.

We need a website design that matches our packaging (see attached assets). This includes the blue/orange color scheme and our key messages:

-Natural relief for back pain
-Soothes using your body's natural energy
-Odorless, Gentle, Easy to Use
-Reusable up to 5 days

We are going to be using the Shopify platform for this website, so we'd like the design to be usable with this theme:
http://pliantframe.tovashelf.com/pages/theme-features

We will do all of the coding, but please keep this layout in mind for the design.

Target Market(s)

The Vorlixa Spine Pad is targeted to people suffering from mild to moderate, chronic back pain, but who desire to continue leading active lives.

Industry/Entity Type

Adhesive

Requirements
Must have
• The design needs to have the same look and feel as the packaging for the back patch. Please feel free to use any of the attached assets in your design (doesn't need to be all).
Should not have
• We do not want to see stock photography other than the assets provided.

```html
<!DOCTYPE html>
<html lang="en">
<head>
<meta charset="utf-8">
<title>Vorlixa Spine Pad</title>
<link rel="stylesheet" href="https://fonts.googleapis.com/css2?family=Ubuntu:ital,wght@0,400;0,500;0,700;1,700&family=Oswald:wght@600&family=Open+Sans:wght@400;600;700&display=swap">
<style>
:root{
  --orange:#f5841f;
  --orange-dark:#e46d0c;
  --blue:#1a6fb8;
  --blue-dark:#0d4f94;
  --blue-deep:#123f85;
  --text:#1e1e1e;
  --grey-panel:#efefef;
  --grey-line:#d4d4d4;
  --white:#ffffff;
}
*{box-sizing:border-box;margin:0;padding:0}
html,body{width:1163px;height:1200px;overflow:hidden}
body{position:relative;background:#fff;font-family:"Open Sans",Arial,sans-serif;color:var(--text)}

/* header */
.site-header{position:absolute;left:0;top:0;width:1163px;height:120px;
  background:linear-gradient(180deg,#8fb6dd 0%,#c9ddef 45%,#eef4fa 100%)}
.brand{position:absolute;left:186px;top:28px;font-family:"Ubuntu",sans-serif;font-weight:700;
  font-size:40px;color:var(--orange);letter-spacing:-0.5px;white-space:nowrap}
.social{position:absolute;top:10px;display:flex;gap:10px;left:873px}
.social span{width:27px;height:27px;border-radius:5px;background:linear-gradient(180deg,#4d8fd0,#1c5fa6);display:block}

/* nav */
.main-nav{position:absolute;left:0;top:120px;width:1163px;height:35px;background:var(--blue);
  border-bottom:1px solid #5d9ad2}
.main-nav ul{list-style:none;display:flex;position:absolute;left:206px;top:9px;gap:21px}
.main-nav li{font-family:"Ubuntu",sans-serif;font-weight:500;font-size:12.5px;color:#fff;text-transform:uppercase;white-space:nowrap}

/* hero */
.hero-band{position:absolute;left:0;top:155px;width:1163px;height:296px;background:var(--orange)}
.hero{position:absolute;left:174px;top:159px;width:815px;height:289px;overflow:hidden;
  background:linear-gradient(90deg,#6b5a48 0%,#9b8a74 25%,#c5b9a8 45%,#7c8ea8 58%,#2d63b6 72%,#1f4fa8 100%)}
.hero-photo{position:absolute;left:0;top:0;width:560px;height:289px}
.hero svg{position:absolute;left:0;top:0}
.hero-tag{position:absolute;left:553px;top:40px;width:245px;height:34px;line-height:34px;text-align:center;
  font-family:"Ubuntu",sans-serif;font-style:italic;font-weight:700;font-size:21px;color:#fff;
  letter-spacing:-0.5px;white-space:nowrap}
.hero-term{position:absolute;right:32px;font-family:"Oswald",sans-serif;font-weight:600;color:#fff;
  font-size:35px;line-height:1;text-align:right;letter-spacing:0.5px;white-space:nowrap}

/* content */
.content-bg{position:absolute;left:0;top:451px;width:1163px;height:608px;
  background:linear-gradient(180deg,#e2e2e2 0%,#ffffff 70px,#ffffff 100%)}
.section-title{position:absolute;font-family:"Ubuntu",sans-serif;font-weight:500;color:var(--orange);font-size:22px;white-space:nowrap}
.intro{position:absolute;left:189px;top:507px;width:556px;font-size:11px;line-height:17px;text-align:justify}

.step{position:absolute;top:642px;width:174px;height:156px;border-radius:8px;
  background:linear-gradient(180deg,#7fc2ea 0%,#f4b58e 30%,#f4b58e 70%,#bfe3f6 100%)}
.step-num{position:absolute;left:6px;top:5px;width:15px;height:15px;border:1.5px solid #fff;border-radius:50%;
  color:#fff;font-size:10px;line-height:12px;text-align:center}
.step-caption{position:absolute;top:803px;width:174px;text-align:center;font-family:Arial,sans-serif;font-size:8.5px;line-height:11px;color:#444}
.step-arrow{position:absolute;top:744px}

.product{position:absolute;top:876px;width:126px;height:105px;border:2px solid var(--orange);background:#fff}
.product .shot{position:absolute;left:10px;top:10px;right:10px;bottom:10px;border-radius:4px}
.product-name{position:absolute;top:985px;font-weight:700;font-size:10.5px;letter-spacing:0.3px;white-space:nowrap}
.product-price{position:absolute;top:1000px;font-size:10.5px;white-space:nowrap}
.btn-cart{position:absolute;top:1017px;width:84px;height:20px;border-radius:3px;
  background:linear-gradient(180deg,#3a8ad6,#1760ab);border:1px solid #0f4d8f;color:#fff;font-size:8px;text-align:center;line-height:18px}

/* news */
.news-item{position:absolute;left:760px;width:215px;height:58px;background:var(--grey-panel);border:1px solid var(--grey-line)}
.news-date{position:absolute;left:6px;top:8px;width:48px;height:43px;border:2px solid var(--orange)}
.news-date .d{height:17px;background:var(--orange);color:#fff;font-weight:700;font-size:10.5px;text-align:center;line-height:17px}
.news-date .y{height:22px;background:var(--blue);color:#fff;font-weight:700;font-size:14px;text-align:center;line-height:22px;font-family:Georgia,serif}
.news-title{position:absolute;left:61px;top:7px;width:150px;font-size:10px;line-height:12px;font-weight:700;color:var(--blue);letter-spacing:0.4px}
.news-meta{position:absolute;left:61px;top:36px;font-size:7px;color:var(--orange)}

/* quick contact */
.contact-shadow{position:absolute;left:730px;top:1010px;width:280px;height:40px;border-radius:50%;
  background:radial-gradient(ellipse,rgba(0,0,0,0.18),rgba(0,0,0,0) 70%)}
.contact-panel{position:absolute;left:761px;top:788px;width:212px;height:251px;border:1px solid #cfcfcf;border-radius:4px;
  background:linear-gradient(90deg,#d9d9d9,#f4f4f4 50%,#d9d9d9)}
.contact-ribbon{position:absolute;left:775px;top:782px}
.contact-title{position:absolute;left:775px;top:800px;width:184px;text-align:center;font-family:"Ubuntu",sans-serif;
  font-weight:700;font-style:italic;font-size:18px;color:#fff;white-space:nowrap}
.field{position:absolute;left:776px;width:181px;background:#fff;border:1px solid #bcbcbc;border-radius:3px;
  font-size:9px;color:#555;padding:4px 10px}
.btn-send{position:absolute;left:791px;top:990px;width:150px;height:27px;border-radius:3px;
  background:linear-gradient(180deg,#2f86d6,#1259a6);color:#fff;font-family:"Ubuntu",sans-serif;font-size:15px;text-align:center;line-height:27px}

/* footer */
.site-footer{position:absolute;left:0;top:1059px;width:1163px;height:114px;background:var(--blue)}
.footer-links{position:absolute;left:0;top:12px;width:1163px;text-align:center;color:#fff;font-size:11px;letter-spacing:0.3px;word-spacing:1px;white-space:nowrap}
.footer-links span.sep{margin:0 9px}
.copyright{position:absolute;left:0;top:1173px;width:1163px;height:27px;background:var(--blue-dark);border-top:1px solid #5d9ad2;
  color:#fff;font-size:8.5px;text-align:center;line-height:26px}
</style>
</head>
<body>

<header class="site-header">
  <div class="brand">Vorlixa Spine Pad</div>
  <div class="social" aria-label="Social links"><span></span><span></span><span></span></div>
</header>

<nav class="main-nav">
  <ul>
    <li>Home</li><li>About Us</li><li>The Vorlixa Patch</li><li>How it Works</li>
    <li>Blog</li><li>FAQ</li><li>Buy Online Now</li><li>Contact Us</li>
  </ul>
</nav>

<div class="hero-band"></div>
<section class="hero">
  <div class="hero-photo" role="img" aria-label="Photo of a runner stretching outdoors wearing the spine pad on her lower back"></div>
  <svg width="815" height="289" viewBox="0 0 815 289">
    <path d="M430 289 C520 120 650 60 815 40 L815 289 Z" fill="#1f54ad" opacity="0.55"/>
    <polygon points="562,33 805,33 790,78 548,78" fill="#fff"/>
    <polygon points="566,37 798,37 785,74 553,74" fill="var(--orange)"/>
    <rect x="660" y="102" width="138" height="47" fill="#1b86cf"/>
    <rect x="561" y="155" width="237" height="48" fill="#1b86cf"/>
    <rect x="630" y="210" width="168" height="47" fill="#1b86cf"/>
    <line x1="432" y1="126" x2="655" y2="126" stroke="#a9c6ea" stroke-width="1"/>
    <line x1="360" y1="182" x2="556" y2="182" stroke="#a9c6ea" stroke-width="1"/>
    <line x1="395" y1="234" x2="625" y2="234" stroke="#a9c6ea" stroke-width="1"/>
  </svg>
  <div class="hero-tag">Reusable up to 5 days</div>
  <div class="hero-term" style="top:108px">Sprains</div>
  <div class="hero-term" style="top:162px">Sore Muscles</div>
  <div class="hero-term" style="top:216px">Backache</div>
</section>

<div class="content-bg"></div>

<h1 class="section-title" style="left:189px;top:470px">Welcome to Vorlixa Spine Pad</h1>
<p class="intro">Lorem Ipsum. Proin gravida nibh vel velit auctor aliquet. Aenean sollicitudin, lorem quis bibendum auctor, nisi elit consequat ipsum, nec sagittis sem nibh id elit. Duis sed odio sit amet nibh vulputate cursus a sit amet mauris. Morbi accumsan ipsum velit. Nam nec tellus a odio tincidunt auctor a ornare odio. Sed non mauris vitae erat consequat auctor eu in elit. Class aptent taciti sociosqu ad litora torquent per conubia nostra, per inceptos himenaeos. Mauris in erat justo. Nullam ac urna eu felis dapibus condimentum sit</p>

<h2 class="section-title" style="left:191px;top:613px">How its works</h2>
<div class="step" style="left:188px" role="img" aria-label="Illustration of a lower back with red pain rings around the spine"><span class="step-num">1</span></div>
<div class="step" style="left:378px" role="img" aria-label="Illustration of the pad placed over the painful area of the lower back"><span class="step-num">2</span></div>
<div class="step" style="left:569px" role="img" aria-label="Illustration of the lower back with green calm rings after using the pad"><span class="step-num">3</span></div>
<svg class="step-arrow" style="left:350px" width="52" height="36" viewBox="0 0 52 36"><polygon points="0,12 32,12 32,2 52,18 32,34 32,24 0,24" fill="var(--orange)" opacity="0.9"/></svg>
<svg class="step-arrow" style="left:541px" width="52" height="36" viewBox="0 0 52 36"><polygon points="0,12 32,12 32,2 52,18 32,34 32,24 0,24" fill="var(--orange)" opacity="0.9"/></svg>
<p class="step-caption" style="left:188px">Discomfort from lower back pain<br>produces surface energy</p>
<p class="step-caption" style="left:378px">Place the Vorlixa™ Patch on the<br>area of discomfort</p>
<p class="step-caption" style="left:569px">Lower back discomfort is decreased<br>due to the Vorlixa™ Patch</p>

<h2 class="section-title" style="left:188px;top:846px">Our Prosucts</h2>
<div class="product" style="left:188px"><div class="shot" role="img" aria-label="Photo of a dark green thermal sock" style="background:radial-gradient(circle,#6b6b48 0%,#8c8c6a 30%,#fff 62%)"></div></div>
<div class="product" style="left:331px"><div class="shot" role="img" aria-label="Photo of colourful gel heat packs" style="background:radial-gradient(circle,#c44fb5 0%,#3a9bd6 35%,#fff 65%)"></div></div>
<div class="product" style="left:474px"><div class="shot" role="img" aria-label="Photo of black heated gloves" style="background:radial-gradient(circle,#2a2a2a 0%,#555 32%,#fff 62%)"></div></div>
<div class="product" style="left:616px"><div class="shot" role="img" aria-label="Photo of a tan heating pad with controller" style="background:radial-gradient(ellipse,#c8ab88 0%,#d9c2a4 38%,#fff 66%)"></div></div>

<p class="product-name" style="left:204px">Lorem Ipsum</p><p class="product-price" style="left:205px">Price $100</p><div class="btn-cart" style="left:204px">Add to Chart</div>
<p class="product-name" style="left:344px">Lorem Ipsum</p><p class="product-price" style="left:345px">Price $100</p><div class="btn-cart" style="left:344px">Add to Chart</div>
<p class="product-name" style="left:482px">Lorem Ipsum</p><p class="product-price" style="left:482px">Price $100</p><div class="btn-cart" style="left:482px">Add to Chart</div>
<p class="product-name" style="left:628px">Lorem Ipsum</p><p class="product-price" style="left:628px">Price $100</p><div class="btn-cart" style="left:628px">Add to Chart</div>

<h2 class="section-title" style="left:759px;top:479px">Latest News</h2>
<article class="news-item" style="top:514px"><div class="news-date"><div class="d">Jan 10</div><div class="y">2013</div></div><p class="news-title">Lorem Ipsum. Proin gravi Proin gravida lorem proin</p><p class="news-meta">10th Jan 2013</p></article>
<article class="news-item" style="top:576px"><div class="news-date"><div class="d">Jan 10</div><div class="y">2013</div></div><p class="news-title">Lorem Ipsum. Proin gravi Proin gravida lorem proin</p><p class="news-meta">10th Jan 2013</p></article>
<article class="news-item" style="top:637px"><div class="news-date"><div class="d">Jan 10</div><div class="y">2013</div></div><p class="news-title">Lorem Ipsum. Proin gravi Proin gravida lorem proin</p><p class="news-meta">10th Jan 2013</p></article>
<article class="news-item" style="top:699px"><div class="news-date"><div class="d">Jan 10</div><div class="y">2013</div></div><p class="news-title">Lorem Ipsum. Proin gravi Proin gravida lorem proin</p><p class="news-meta">10th Jan 2013</p></article>

<div class="contact-shadow"></div>
<div class="contact-panel"></div>
<svg class="contact-ribbon" width="184" height="66" viewBox="0 0 184 66">
  <rect x="0" y="0" width="184" height="8" rx="3" fill="#222"/>
  <path d="M3 4 H181 V44 Q92 72 3 44 Z" fill="var(--blue)"/>
  <path d="M3 4 H181 V22 Q92 34 3 22 Z" fill="#2a86d4"/>
</svg>
<div class="contact-title">QUICK CONTACT</div>
<div class="field" style="top:861px;height:20px">Name</div>
<div class="field" style="top:889px;height:21px">Email</div>
<div class="field" style="top:916px;height:64px">Message</div>
<div class="btn-send">Send</div>

<footer class="site-footer">
  <p class="footer-links">Home<span class="sep">|</span>About Us<span class="sep">|</span>The Vorlixa Patch<span class="sep">|</span>How It Works<span class="sep">|</span>Blog<span class="sep">|</span>FAQ<span class="sep">|</span>Buy Online Now<span class="sep">|</span>Contact Us</p>
</footer>
<div class="copyright">Copyright 2013 &nbsp;Vorlixa Spine Pad. All rights reserved.</div>

</body>
</html>
```